VitaQuorb Web Design. Health and Wellness Industry

We are in process of creating next big Cloud based Health Care Management system. We have created 1st draft of Landing Page design. It is missing curb appeal, jazzy feel and engaging modern look.

Need a talented designer to recreate UI/ UX and take it to the next level.
If you are a creative designer, gifted with vision and imagination, I strongly encourage you to participate.

I want the designers to stay focus on the Landing page
Once we select the winner we will provide other subsequent pages
Follow up pages will be similar simple design

Target Market(s)

Individual Users and small business
Age Group 35-75
Individuals involved in "Health and Fitness" activity tracking, managing etc.

Industry/Entity Type

Health And Wellness

Number of Pages Required

5+ page

Colors
f68e4e
34a6d7

Requirements
Must have
• Super Engaging UI/ UX
• Smart and Contemporary look
• Easy to Navigate
• Folder Style menu bar
• Slideshow
• Social Medial Friendly
• Online Shopping
Nice to have
• Start from the enclosed draft Landing Page Idea.
• Feel Free to include additional frame, information section, Icon etc.

```html
<!DOCTYPE html>
<html lang="en">
<head>
<meta charset="utf-8">
<title>VitaQuorb – Cloud Health Care Management</title>
<link href="https://fonts.googleapis.com/css2?family=Open+Sans:wght@300;400;600;700&display=swap" rel="stylesheet">
<style>
:root{
  --orange:#f68e4e;
  --blue:#34a6d7;
  --green:#9cc63f;
  --green-dark:#86b02f;
  --ink:#333;
  --muted:#888;
  --line:#e3e3e3;
  --paper:#fff;
  --soft:#f3f3f3;
  --footer:#2d2d2d;
  --footer-base:#222;
}
*{box-sizing:border-box;margin:0;padding:0}
html,body{width:1200px;height:2652px;overflow:hidden}
body{font-family:"Open Sans",Arial,sans-serif;color:var(--ink);background:var(--paper);font-size:13px;line-height:1.6}
.page{position:relative;width:1200px;height:2652px}

/* header */
.site-header{height:108px;display:flex;align-items:center;padding:0 40px;background:var(--paper)}
.brand{display:flex;align-items:center;gap:8px;width:220px}
.brand-mark{width:24px;height:24px;border-radius:50%;background:var(--orange)}
.brand-name{font-size:28px;font-weight:600;color:var(--orange);letter-spacing:-.5px}
.main-nav{display:flex;gap:34px;margin-left:20px;font-size:14px;font-weight:600;color:#555}
.main-nav .active{color:var(--orange)}
.header-tools{margin-left:auto;text-align:right}
.btn-app{display:inline-block;background:var(--blue);color:#fff;font-size:12px;font-weight:700;padding:9px 26px;border-radius:2px;letter-spacing:.5px}
.account-links{font-size:11px;color:var(--muted);margin-top:8px;display:flex;gap:10px;justify-content:flex-end;align-items:center}
.cart{width:16px;height:14px}

/* hero */
.hero{position:relative;height:472px;background:linear-gradient(100deg,#2f86c4 0%,#58b2e4 45%,#a9d8f2 100%)}
.hero-photo{position:absolute;inset:0;background:linear-gradient(100deg,rgba(20,90,160,.55) 0%,rgba(60,150,210,.25) 55%,rgba(200,230,248,.35) 100%)}
.hero-copy{position:absolute;left:140px;top:80px;width:470px;color:#fff}
.hero-copy h1{font-size:30px;font-weight:300;line-height:1.2}
.hero-copy h2{font-size:17px;font-weight:400;margin-top:4px}
.hero-copy p{font-size:12px;margin-top:14px;opacity:.92}
.btn-orange{display:inline-block;background:var(--orange);color:#fff;font-size:11px;font-weight:700;padding:9px 22px;border-radius:2px;letter-spacing:.5px}
.hero-copy .btn-orange{margin-top:24px}
.slider-dots{position:absolute;bottom:22px;left:50%;transform:translateX(-50%);display:flex;gap:8px}
.slider-dots span{width:9px;height:9px;border-radius:50%;background:rgba(255,255,255,.55)}
.slider-dots .on{background:#fff}

/* intro */
.intro{display:flex;gap:40px;padding:40px 40px 0 50px;height:420px}
.section-label{font-size:18px;font-weight:400;color:var(--blue);padding-bottom:10px;border-bottom:1px solid var(--line);margin-bottom:24px}
.how-it-works{width:500px}
.step{display:flex;gap:20px;margin-bottom:26px}
.step-thumb{width:160px;height:100px;flex:none;background:linear-gradient(135deg,#b9cfe4,#e8eef5)}
.step h3{font-size:15px;font-weight:600}
.meta{font-size:11px;color:var(--orange)}
.step p,.overview-text p{font-size:11px;color:var(--muted)}
.more{color:var(--orange)}
.overview{flex:1}
.overview-body{display:flex;gap:24px}
.overview-photo{width:270px;height:200px;flex:none;background:linear-gradient(135deg,#d7e7f2,#8fbcd9)}
.overview-text h3{font-size:14px;font-weight:600;margin-bottom:8px}
.overview .btn-orange{margin-top:16px}

/* discover */
.discover{height:480px;background:var(--green);color:#fff;position:relative}
.discover-title{text-align:center;font-size:18px;font-weight:400;padding-top:26px;letter-spacing:.5px}
.discover-body{display:flex;gap:50px;padding:36px 0 0 190px}
.discover-frame{width:360px;height:280px;background:#fff;padding:8px;box-shadow:0 3px 10px rgba(0,0,0,.2)}
.discover-photo{width:100%;height:100%;background:linear-gradient(135deg,#c6dbe8,#5e8fb0)}
.discover-copy{width:420px;font-size:12px}
.discover-copy h3{font-size:18px;font-weight:400;margin:22px 0 10px}
.btn-outline{display:inline-block;border:1px solid #fff;padding:8px 28px;font-size:12px;margin-top:18px}

/* products */
.products{height:480px;background:var(--soft);text-align:center}
.products-title{font-size:18px;font-weight:400;color:var(--blue);padding-top:34px}
.product-row{display:flex;justify-content:center;gap:40px;margin-top:36px}
.product{width:250px}
.product-photo{height:180px;background:#fff;border:1px solid var(--line);display:flex;align-items:center;justify-content:center}
.product-photo div{width:120px;height:120px;border-radius:10px;background:linear-gradient(135deg,#555,#222)}
.product-photo .light{background:linear-gradient(135deg,#f2f2f2,#c8c8c8)}
.product h4{font-size:14px;font-weight:600;margin-top:14px}
.price{font-size:11px;margin-top:4px}
.price .now{color:var(--orange);margin-right:6px}
.price .cart-link{color:var(--blue);font-weight:600}
.btn-blue{display:inline-block;background:var(--blue);color:#fff;font-size:12px;font-weight:700;padding:11px 26px;border-radius:2px;margin-top:36px;letter-spacing:.5px}

/* feedback */
.feedback-band{height:56px;background:var(--green);color:#fff;text-align:center;font-size:18px;line-height:56px}
.testimonials{height:284px;display:flex;justify-content:center;gap:80px;padding-top:50px}
.testimonial{display:flex;gap:24px;width:440px}
.avatar{width:140px;height:140px;border-radius:50%;flex:none;background:linear-gradient(135deg,#d9d2c8,#8a7b6c);border:4px solid #eee}
.quote{font-size:12px;color:#666;padding-top:18px}
.quote .more{display:block;margin-top:6px}

/* footer */
.site-footer{height:280px;background:var(--footer);color:#ccc;display:flex;gap:40px;padding:34px 0 0 100px}
.footer-col{width:230px}
.footer-col h5{font-size:14px;font-weight:600;color:#fff;margin-bottom:12px}
.footer-col li{list-style:none;font-size:10px;line-height:2;text-transform:uppercase;color:#bbb}
.footer-base{height:52px;background:var(--footer-base);color:#999;font-size:11px;text-align:center;line-height:52px;position:relative}
.social{position:absolute;right:60px;top:18px;display:flex;gap:8px}
.social span{width:16px;height:16px;border-radius:50%;background:#555}
</style>
</head>
<body>
<div class="page">

  <header class="site-header">
    <div class="brand"><span class="brand-mark"></span><span class="brand-name">VitaQuorb</span></div>
    <nav class="main-nav">
      <span class="active">Home</span><span>Discover HealthNook</span><span>Shop</span><span>Caregiver</span><span>Community</span>
    </nav>
    <div class="header-tools">
      <span class="btn-app">DOWNLOAD FREE APP</span>
      <div class="account-links">
        <span>Login</span><span>|</span><span>Register</span><span>|</span><span>My account</span>
        <svg class="cart" viewBox="0 0 16 14"><path d="M1 1h3l2 8h8l1.5-6H5" fill="none" stroke="#888" stroke-width="1.5"/><circle cx="7" cy="12" r="1.3" fill="#888"/><circle cx="13" cy="12" r="1.3" fill="#888"/></svg>
      </div>
    </div>
  </header>

  <section class="hero">
    <div class="hero-photo" role="img" aria-label="Doctor's hand touching a glowing medical interface with heartbeat line"></div>
    <div class="hero-copy">
      <h1>You Need a Professional</h1>
      <h2>Give us a call to discuss how we can help you</h2>
      <p>Our care team works with you to track daily health, plan routines and keep records safe in the cloud. Talk to us today and see how simple managing wellness for you and your family can be.</p>
      <span class="btn-orange">READ MORE</span>
    </div>
    <div class="slider-dots"><span class="on"></span><span></span><span></span><span></span></div>
  </section>

  <section class="intro">
    <div class="how-it-works">
      <h2 class="section-label">HOW IT WORKS</h2>
      <article class="step">
        <div class="step-thumb" role="img" aria-label="Patient using a health app"></div>
        <div>
          <h3>Energetic startup subsidiar</h3>
          <div class="meta">June 9, 2015</div>
          <p>Track your vitals and activity in one place, then share progress with your care team in seconds. <span class="more">MORE</span></p>
        </div>
      </article>
      <article class="step">
        <div class="step-thumb" role="img" aria-label="Doctor reviewing a chart with a patient"></div>
        <div>
          <h3>Energetic startup lorean</h3>
          <div class="meta">June 9, 2015</div>
          <p>Book visits, get reminders and keep every report organised with secure cloud storage. <span class="more">MORE</span></p>
        </div>
      </article>
    </div>
    <div class="overview">
      <h2 class="section-label">OVERVIEW</h2>
      <div class="overview-body">
        <div>
          <div class="overview-photo" role="img" aria-label="Group of smiling medical staff in scrubs"></div>
          <span class="btn-orange">READ MORE</span>
        </div>
        <div class="overview-text">
          <h3>Plan goals with our care team, check results and get support when needed.</h3>
          <p>Our platform brings records, devices and caregivers together so you always know where your health stands. Set reminders, log meals and sleep, and see weekly trends at a glance.</p>
          <p>Built for individuals and small practices who want clear, simple tools.</p>
        </div>
      </div>
    </div>
  </section>

  <section class="discover">
    <h2 class="discover-title">DISCOVER HEALTHNOOK</h2>
    <div class="discover-body">
      <div class="discover-frame"><div class="discover-photo" role="img" aria-label="Scientist looking through a laboratory microscope"></div></div>
      <div class="discover-copy">
        <p>Store lab results, prescriptions and device readings in one private space. Invite family or doctors to view only what you choose, from any device.</p>
        <p>Secure sync keeps your data current, while clear charts show progress on weight, heart rate and sleep over time.</p>
        <h3>Cloud based Health Care Management</h3>
        <p>From daily steps to yearly check-ups, everything stays organised, backed up and ready whenever you need it most.</p>
        <span class="btn-outline">Get Started</span>
      </div>
    </div>
  </section>

  <section class="products">
    <h2 class="products-title">FEATURED PRODUCTS</h2>
    <div class="product-row">
      <div class="product">
        <div class="product-photo"><div role="img" aria-label="Black activity tracker wristband"></div></div>
        <h4>PulseTrack Edge</h4>
        <div class="price"><span class="now">$70</span><span class="cart-link">ADD TO CART</span></div>
      </div>
      <div class="product">
        <div class="product-photo"><div class="light" role="img" aria-label="White fingertip pulse oximeter"></div></div>
        <h4>Wireless Pulse Oximeter</h4>
        <div class="price"><span class="now">$70</span><span class="cart-link">ADD TO CART</span></div>
      </div>
      <div class="product">
        <div class="product-photo"><div role="img" aria-label="Black glass body scale"></div></div>
        <h4>Wireless Body Scale</h4>
        <div class="price"><span class="now">$70</span><span class="cart-link">ADD TO CART</span></div>
      </div>
    </div>
    <span class="btn-blue">BROWSE MORE PRODUCTS</span>
  </section>

  <h2 class="feedback-band">OUR CUSTOMERS' FEEDBACK</h2>
  <section class="testimonials">
    <article class="testimonial">
      <div class="avatar" role="img" aria-label="Portrait of a customer"></div>
      <p class="quote">I recommend this team to anyone who wants clear health tracking. Setup was quick and support is friendly and helpful.<span class="more">Read more</span></p>
    </article>
    <article class="testimonial">
      <div class="avatar" role="img" aria-label="Portrait of a customer"></div>
      <p class="quote">I recommend this team to anyone who wants clear health tracking. My records are finally in one simple place.<span class="more">Read more</span></p>
    </article>
  </section>

  <footer class="site-footer">
    <div class="footer-col"><h5>COMPANY</h5><ul><li>Home</li><li>Shop</li><li>Contact &amp; Benefits</li><li>Video</li><li>FAQ</li><li>Downloads</li><li>Testimonials</li></ul></div>
    <div class="footer-col"><h5>PRODUCTS</h5><ul><li>Wireless Scales</li><li>Testimonials</li><li>Press</li><li>Auto Renewal</li><li>Terms &amp; Conditions</li><li>Privacy Policy</li></ul></div>
    <div class="footer-col"><h5>DOWNLOADS</h5><ul><li>How It Works</li><li>Video</li><li>Instructions</li><li>FAQ</li><li>Education</li></ul></div>
    <div class="footer-col"><h5>DOWNLOADS</h5><ul><li>How It Works</li><li>Video</li><li>Instructions</li><li>FAQ</li><li>Education</li></ul></div>
  </footer>
  <div class="footer-base">© Copyright 2015. VitaQuorb. All rights reserved
    <div class="social"><span></span><span></span><span></span></div>
  </div>

</div>
</body>
</html>
```